Brightvolt Electrical Services Needs A Flyer Design

We need a flyer design for a new business based in Sydney, Australia called Brightvolt Electrical Services. We provide services for residential,commercial and industrial works. Services include Electrical Design, Installation, Repairs & Maintenance. Communications Installation, Cabling, Maintenance & Repairs. Over 25 years Industry Experience.Service Calls, Quick Response Time, Professional Service. We would like to see designs that use the colors red,white and blue similar to the logo. The final Design should be creative as the business logo suggests and should communicate the businesses services.

Target Market(s)

Residential

Industry/Entity Type

Industrial

Font styles to use
Sans Serif

Requirements
Must have
• My project must have the logo provided utilized in the flyer.It must list the following contact name and number Ray 0491 627 318 services as above in the project description. Flyer should be DL size (99mmx210mm).

```html
<!DOCTYPE html>
<html lang="en">
<head>
<meta charset="utf-8">
<title>Brightvolt Electrical Services – Flyer</title>
<link href="https://fonts.googleapis.com/css2?family=Baloo+2:wght@400;600;700&family=Arimo:wght@400;700&display=swap" rel="stylesheet">
<style>
  :root {
    --orange: #f5821f;
    --slate: #5b5d60;
    --white: #ffffff;
    --navy: #1c2a56;
    --ink: #111111;
  }
  html, body {
    margin: 0;
    padding: 0;
    overflow: hidden;
  }
  .flyer {
    position: relative;
    width: 1200px;
    height: 2545px;
    background: var(--slate);
    overflow: hidden;
    font-family: "Arimo", Arial, sans-serif;
  }
  .flyer__shapes {
    position: absolute;
    inset: 0;
  }
  .block {
    position: absolute;
    left: 0;
    width: 100%;
    text-align: center;
    margin: 0;
  }
  .brand {
    top: 500px;
    color: var(--navy);
    font-family: "Baloo 2", sans-serif;
    font-weight: 700;
    line-height: 1;
  }
  .brand__name {
    display: block;
    font-size: 128px;
    letter-spacing: 6px;
  }
  .brand__sub {
    display: block;
    font-size: 40px;
    letter-spacing: 5px;
    margin-top: 4px;
  }
  .experience {
    top: 718px;
    font-family: "Baloo 2", sans-serif;
    font-weight: 400;
    font-size: 68px;
    line-height: 74px;
    color: var(--orange);
  }
  .promise {
    top: 900px;
    font-weight: 700;
    font-size: 40px;
    line-height: 56px;
    color: var(--ink);
  }
  .sectors {
    top: 1252px;
    font-family: "Baloo 2", sans-serif;
    font-weight: 700;
    font-size: 88px;
    line-height: 91px;
    color: var(--orange);
  }
  .divider {
    position: absolute;
    top: 1660px;
    left: 262px;
    width: 676px;
    height: 4px;
    background: var(--white);
  }
  .services {
    top: 1700px;
    color: var(--white);
    font-size: 43px;
    line-height: 60px;
  }
  .services__title {
    display: block;
    font-weight: 700;
    color: var(--orange);
    font-size: 44px;
  }
  .services__list {
    list-style: none;
    margin: 0;
    padding: 0;
  }
  .contact {
    top: 2318px;
  }
  .contact__label {
    display: block;
    font-size: 56px;
    color: var(--ink);
    line-height: 70px;
  }
  .contact__phone {
    display: block;
    font-family: "Baloo 2", sans-serif;
    font-weight: 700;
    font-size: 86px;
    line-height: 100px;
    color: var(--orange);
  }
</style>
</head>
<body>
<main class="flyer">
  <svg class="flyer__shapes" width="1200" height="2545" viewBox="0 0 1200 2545" aria-hidden="true">
    <rect x="0" y="0" width="1200" height="300" fill="var(--white)"/>
    <ellipse cx="600" cy="15" rx="400" ry="230" fill="var(--white)" stroke="var(--orange)" stroke-width="60"/>
    <ellipse cx="600" cy="662" rx="567" ry="446" fill="var(--white)" stroke="var(--orange)" stroke-width="66"/>
    <ellipse cx="600" cy="2560" rx="590" ry="370" fill="var(--white)" stroke="var(--orange)" stroke-width="66"/>
  </svg>

  <h1 class="block brand">
    <span class="brand__name">BRIGHTVOLT</span>
    <span class="brand__sub">ELECTRICAL SERVICES</span>
  </h1>

  <p class="block experience">Over 25 years<br>Industry Experience.</p>

  <p class="block promise">Service Calls, Quick Response<br>Time, Professional Service.</p>

  <h2 class="block sectors">Residential<br>Commercial<br>and<br>Industrial Works</h2>

  <div class="divider"></div>

  <section class="block services">
    <span class="services__title">Services include:</span>
    <ul class="services__list">
      <li>Electrical Design</li>
      <li>Installation</li>
      <li>Repairs &amp; Maintenance</li>
      <li>Communications Installation</li>
      <li>Cabling</li>
      <li>Maintenance &amp; Repairs</li>
    </ul>
  </section>

  <p class="block contact">
    <span class="contact__label">Contact:</span>
    <span class="contact__phone">Ray 0491 627 318</span>
  </p>
</main>
</body>
</html>
```